Lionel Arbusto and Dwight Halvorsen Advertisement

We would like an ad that conveys understated elegance. We are a company that purchases estate jewelry watches and diamonds. We care to a wealthy, upscale clientele.

Target Market(s)

Wealthy upscale.

Industry/Entity Type

It Company

Requirements
Must have
• Elegant Design. Crisp Clean. Attached a doc of how the ad should be arranged.

```html
<!DOCTYPE html>
<html lang="en">
<head>
<meta charset="utf-8">
<title>Lionel Arbusto &amp; Dwight Halvorsen — Ready to Sell?</title>
<link href="https://fonts.googleapis.com/css2?family=Pinyon+Script&family=Sorts+Mill+Goudy&family=Cinzel:wght@400&family=Libre+Baskerville&display=swap" rel="stylesheet">
<style>
  :root {
    --page-white: #ffffff;
    --ad-black: #0c0c0c;
    --silver-light: #f2f2f2;
    --silver-mid: #b9b9b9;
    --silver-dark: #5e5e5e;
    --text-white: #ecebe8;
    --text-soft: #d6d6d6;
  }
  * { margin: 0; padding: 0; box-sizing: border-box; }
  html, body {
    width: 1000px;
    height: 1200px;
    overflow: hidden;
    background: var(--page-white);
  }
  .ad {
    position: absolute;
    left: 102px;
    top: 18px;
    width: 796px;
    height: 1162px;
    overflow: hidden;
    background:
      radial-gradient(ellipse 520px 300px at 90% 2%, rgba(90,90,90,0.45), transparent 70%),
      radial-gradient(ellipse 380px 700px at 98% 75%, rgba(70,70,70,0.45), transparent 70%),
      radial-gradient(ellipse 420px 360px at 8% 48%, rgba(60,60,60,0.35), transparent 70%),
      linear-gradient(180deg, #141414 0%, var(--ad-black) 50%, #111 100%);
    text-align: center;
  }
  .headline {
    position: absolute;
    left: 0; right: 0;
    top: 52px;
    font-family: "Pinyon Script", cursive;
    font-weight: 400;
    font-size: 110px;
    line-height: 1.2;
    background: linear-gradient(180deg, var(--silver-light) 20%, var(--silver-mid) 60%, #7a7a7a 100%);
    -webkit-background-clip: text;
    background-clip: text;
    color: transparent;
  }
  .gem-visual {
    position: absolute;
    left: 270px;
    top: 262px;
    width: 270px;
    height: 240px;
    transform: rotate(14deg);
    clip-path: polygon(8% 0, 92% 0, 100% 10%, 100% 90%, 92% 100%, 8% 100%, 0 90%, 0 10%);
    background:
      radial-gradient(ellipse at 70% 20%, #ffffff 0%, transparent 45%),
      linear-gradient(135deg, #f4f4f6 0%, #c9cbd0 35%, #eeeff2 55%, #9ea1a8 80%, #dcdde0 100%);
  }
  .brand-name {
    position: absolute;
    left: 0; right: 0;
    top: 744px;
    font-family: "Cinzel", serif;
    font-weight: 400;
    font-size: 15.5px;
    letter-spacing: 0.3px;
    color: var(--text-soft);
  }
  .promise {
    position: absolute;
    left: 0; right: 0;
    top: 866px;
    font-family: "Sorts Mill Goudy", serif;
    font-size: 50px;
    line-height: 1.1;
    background: linear-gradient(90deg, var(--silver-dark) 0%, var(--silver-light) 50%, var(--silver-dark) 100%);
    -webkit-background-clip: text;
    background-clip: text;
    color: transparent;
  }
  .appointment {
    position: absolute;
    left: 0; right: 0;
    top: 956px;
    font-family: "Sorts Mill Goudy", serif;
    font-size: 36px;
    line-height: 1.1;
    color: var(--text-white);
  }
  .contact {
    position: absolute;
    left: 0; right: 0;
    top: 1006px;
    font-family: "Libre Baskerville", serif;
    font-size: 17px;
    line-height: 26.5px;
    letter-spacing: 1.4px;
    color: var(--text-soft);
    font-style: normal;
  }
</style>
</head>
<body>
  <main class="ad">
    <h1 class="headline">Ready to Sell?</h1>

    <div class="gem-visual" role="img" aria-label="Emerald-cut diamond, brilliant white on black"></div>

    <p class="brand-name">LIONEL ARBUSTO &amp; DWIGHT HALVORSEN</p>

    <p class="promise">Utmost Discretion</p>
    <p class="appointment">By Appointment</p>

    <address class="contact">
      Casa Lumina | 118-B Coral Promenade<br>
      Seabright, FL 33999<br>
      support@arbustohalvorsen.com<br>
      555.014.2290
    </address>
  </main>
</body>
</html>
```